Corporate speaking flyer for email

Redesign existing and very lame flyer. This is for my speaking business to be used as an introduction of content and style and my presentations. More photos can be provided. As you will see I'm an adventurer who makes part of my living from speaking about my adventures. The bio describes the general gist of that. There is more I could say but wanting to keep it pretty brief so as not to bore potential clients. Having said that I'd like to try and capture them in the first instance.

Target Market(s)

Corporate, clubs, events

Industry/Entity Type

Business

Requirements
Must have
• bio and references. Content provided. Feel free to edit.
Nice to have
• Surprise me!
Should not have
• Rude words.

```html
<!DOCTYPE html>
<html lang="en">
<head>
<meta charset="utf-8">
<title>Sam Calder – Speaker</title>
<link href="https://fonts.googleapis.com/css2?family=Bodoni+Moda:ital,wght@0,600;1,600&family=Source+Sans+3:ital,wght@0,400;0,600;0,700;1,600&display=swap" rel="stylesheet">
<style>
:root{
  --navy:#0f1f4a;
  --blue:#2f58b8;
  --green:#3aa84b;
  --ink:#1a2550;
  --white:#ffffff;
  --rule:#c9d3ea;
}
*{margin:0;padding:0;box-sizing:border-box}
html,body{width:927px;height:1200px;overflow:hidden;background:var(--white)}
body{position:relative;font-family:"Source Sans 3",sans-serif;color:var(--ink)}
.hero{position:absolute;left:0;top:0;width:927px;height:410px;
  background:linear-gradient(90deg,#2a2a2e 0%,#4a4c55 35%,#2c4a90 62%,#1f3f9a 100%)}
.title{position:absolute;left:470px;top:40px;width:430px;text-align:center;color:var(--white);
  font-family:"Bodoni Moda",serif;font-weight:600;line-height:.9}
.title .first{font-size:86px;letter-spacing:1px}
.title .last{font-size:84px;letter-spacing:-2px}
.rule{position:absolute;left:532px;width:288px;height:1px;background:var(--rule)}
.tagline{position:absolute;left:498px;top:226px;width:380px;color:var(--white);
  font-family:"Bodoni Moda",serif;font-style:italic;font-size:47px;line-height:1.05}
.tagline .l1{display:block;padding-left:18px}
.tagline .l2{display:block;padding-left:104px}
.contact{position:absolute;left:480px;top:368px;width:400px;text-align:center;color:var(--white);
  font-size:13.5px;font-weight:700;line-height:18px}
.panel{position:absolute;left:31px;top:442px;width:250px;height:720px;border-radius:10px;
  background:linear-gradient(180deg,var(--green) 0%,#1d6a55 38%,#153a5a 70%,var(--navy) 100%);
  color:var(--white);text-align:center}
.portrait{position:absolute;left:40px;top:312px;width:240px;height:240px;border-radius:50%;
  border:9px solid var(--white);background:radial-gradient(circle,#8a9a8a,#4e5a52)}
.book{position:absolute;left:242px;top:315px;width:98px;height:171px;
  background:linear-gradient(180deg,#6fb0d8 0%,#3c86bf 60%,#1f5d90 100%);box-shadow:3px 3px 6px rgba(0,0,0,.35)}
.panel h2{position:absolute;top:112px;left:0;width:100%;font-family:"Bodoni Moda",serif;font-weight:600;
  font-size:20px;line-height:22px;letter-spacing:.3px}
.quote{position:absolute;left:10px;width:230px;font-size:17.5px;line-height:19.8px}
.quote .mark{position:absolute;font-family:"Bodoni Moda",serif;font-size:70px;line-height:1;color:rgba(255,255,255,.25)}
.quote .open{left:0;top:-12px}
.quote .close{right:-6px;bottom:-40px}
.who{position:absolute;left:0;width:100%;font-size:20.5px;line-height:21px;font-weight:600}
.divider{position:absolute;left:25px;width:190px;height:1px;background:rgba(255,255,255,.6)}
.intro{position:absolute;left:314px;top:446px;width:574px;text-align:center;font-style:italic;font-weight:600;
  font-size:19.5px;line-height:23px;color:var(--ink)}
.bio{position:absolute;left:314px;top:528px;width:580px;font-size:14.6px;line-height:16.6px;color:var(--ink)}
.bio p{margin-bottom:16.6px}
.bio b{font-weight:700}
</style>
</head>
<body>
<div class="hero" role="img" aria-label="Speaker presenting to an audience in front of a projection screen"></div>
<h1 class="title"><span class="first">SAM</span><br><span class="last">CALDER</span></h1>
<div class="rule" style="top:220px"></div>
<p class="tagline"><span class="l1">“Anything</span><span class="l2">is Possible”</span></p>
<div class="rule" style="top:330px"></div>
<p class="contact">sam@tidemail.co.nz &nbsp;/&nbsp; www.samcalder.com<br>+64 (0)21 000 12345 &nbsp;/&nbsp; +64 (0)7 000 6789</p>

<section class="panel">
  <h2>WHAT CLIENTS<br>ARE SAYING...</h2>
  <div class="quote" style="top:172px"><span class="mark open">“</span>One regular conference goer said I could organise another 50 conferences and not see a presentation as good as that.<span class="mark close">”</span></div>
  <p class="who" style="top:282px">LEONARD FIRTH,<br>Fuelworks</p>
  <div class="divider" style="top:340px"></div>
  <div class="quote" style="top:364px"><span class="mark open">“</span>… hearing your story was more inspirational than all the traditional "motivational" type trainers put together.<span class="mark close">”</span></div>
  <p class="who" style="top:474px">MARK PENROSE,<br>Penrose Realty</p>
  <div class="divider" style="top:532px"></div>
  <div class="quote" style="top:558px"><span class="mark open">“</span>Sam was unbelievable, amazing, so well received, such a lovely guy, so humble. Had some of the audience in tears.<span class="mark close">”</span></div>
  <p class="who" style="top:668px">COLIN MARSH,<br>Harbourline Country Head</p>
</section>
<div class="portrait" role="img" aria-label="Speaker receiving flowers while being filmed"></div>
<div class="book" role="img" aria-label="Cover of the book The Open Ocean Rower showing a rowing boat at sea"></div>

<p class="intro">Whether it’s laugh out loud humour, inspiration or thought provoking anecdotes and perspective, SAM CALDER’s deeply moving presentations has it all.</p>

<div class="bio">
  <p>“An extraordinary mental and physical effort – something very, very special” is how Sir Martin Hale described Sam Calder and the late Tom Reeve’s incredible achievement in winning the inaugural Atlantic Rowing Race.</p>
  <p>Marathon rowing champion Sam Calder has been a New Zealand International rowing representative for 16 years. Sam’s numerous rowing achievements include World Champs silver, Commonwealth gold and a world record on the indoor rowing machine.</p>
  <p>Sam represented New Zealand at the Atlanta Olympics and published ‘The Open Ocean Rower’ on how he and Tom Reeve captured headlines around the world winning the grueling and inaugural Atlantic Rowing Race in 41 days. He then led teams to successful defenses in the next two editions making it a 3-peat of victories for New Zealand.</p>
  <p>He is co-organiser of the ‘River Run 100’ (<b>www.RiverRun100.kiwi</b>), ‘The River Clash’ (<b>www.TheRiverClash.co.nz</b>), an annual rowing 8s clash between Waikato and leading overseas university crews on the Waikato River. His also recently conceived and managed a rowing expedition across the Tasman Sea.</p>
  <p>Ambitious goal-setting, teamwork and overcoming adversity in multiple Atlantic Rowing Race campaigns is the spine of Sam’s presentations, sandwiching the challenge of following his brother Neil’s journey into Cambodia’s Khmer Rouge genocide <b>www.BrotherJourney.co.nz</b> (optional topic). Powerful inspiring messages on tenacity, hope, love and the last human freedom: the power to choose your attitude and how you respond in a given situation. The humour, the insights and the emotional turning points have audiences spellbound.</p>
  <p>Sam will inspire you to pursue your dreams whatever they may be, to take on new challenges, overcoming hardship against the odds and know that with passion anything is possible!</p>
  <p>It doesn’t hurt to be just a little bit crazy too!</p>
  <p><b>Sam’s life is about following the dream, decision making, commitment, team building, goal setting, planning, focus, determination, positive thinking and, of course, winning!</b></p>
</div>
</body>
</html>
```